Business cards for financial advisor-insurance agent firm

Our company, Marlowe Pettigrew Insurance & Investments, is an insurance (health, life, home, auto, etc) and investment brokerage offering a suite of options to meet client needs. We need business cards that are professional and embody strength, security and sophistication.

Also running a letterhead project at
http://briefs.artboardhub.com/brief.aspx?id=517962

Target Market(s)

Upper middle class and wealthy

Industry/Entity Type

Investment

Requirements
Nice to have
• Looking for either white, navy blue, or gray cards

```html
<!DOCTYPE html>
<html lang="en">
<head>
<meta charset="utf-8">
<title>Marlowe Pettigrew Insurance &amp; Investments — Business Cards</title>
<link rel="stylesheet" href="https://fonts.googleapis.com/css2?family=Cinzel:wght@400;500&family=Open+Sans:wght@400&display=swap">
<style>
  :root {
    --navy: #2f3858;
    --navy-deep: #262d48;
    --navy-light: #3d4870;
    --steel: #8ea3b0;
    --steel-pale: #a9b9c3;
    --silver: #c8ccd2;
    --paper: #ffffff;
    --paper-shade: #e9eaec;
    --ink: #2b2f3c;
    --backdrop: #e4e2de;
  }
  * { margin: 0; padding: 0; box-sizing: border-box; }
  html, body { width: 1200px; height: 1024px; overflow: hidden; background: var(--backdrop); }
  .canvas { position: relative; width: 1200px; height: 1024px; }

  .card { position: absolute; left: 250px; width: 700px; height: 400px; overflow: hidden;
          box-shadow: 0 6px 18px rgba(0,0,0,.18); }
  .card--front { top: 52px; background: linear-gradient(135deg, var(--paper) 0%, var(--paper-shade) 100%); }
  .card--back  { top: 572px; background: radial-gradient(ellipse at 45% 35%, var(--navy-light) 0%, var(--navy) 55%, var(--navy-deep) 100%); }

  .brand { position: absolute; font-family: "Cinzel", serif; font-weight: 500; letter-spacing: .02em; }
  .brand__mark { display: block; width: 38px; height: 38px; border: 2px solid var(--navy); margin-bottom: 10px; }
  .brand__name { display: block; font-size: 27px; color: var(--navy); line-height: 1; }
  .brand__tagline { display: block; font-family: "Cinzel", serif; font-weight: 400; font-size: 10.5px;
                    letter-spacing: .08em; color: var(--navy); margin-top: 6px; padding-left: 34px; }

  .card--front .brand { left: 58px; top: 62px; }

  .divider { position: absolute; height: 1px; background: var(--ink); }
  .divider--main { left: 58px; top: 196px; width: 352px; }
  .divider--tail { left: 640px; top: 196px; width: 40px; }

  .holder { position: absolute; left: 420px; top: 182px; font-family: "Cinzel", serif; color: var(--ink); }
  .holder__name { font-size: 21px; font-weight: 400; line-height: 1; }
  .holder__title { font-size: 14px; margin-top: 16px; padding-left: 8px; letter-spacing: .04em; }

  .contacts { position: absolute; left: 58px; top: 222px; list-style: none;
              font-family: "Open Sans", sans-serif; font-size: 15px; color: var(--ink); }
  .contacts li { display: flex; align-items: center; height: 31px; }
  .contacts .icon { width: 19px; height: 19px; margin-right: 12px; flex: none; }

  .band { position: absolute; left: 0; right: 0; bottom: 0; }
  .card--front .band { height: 58px; background: var(--steel); }
  .card--front .band__accent { position: absolute; right: 0; top: 0; bottom: 0; width: 96px; background: var(--navy); }
  .card--back .band { height: 44px; background: var(--steel); }
  .card--back .band__accent { position: absolute; left: 0; top: 0; bottom: 0; width: 84px; background: var(--silver); }

  .card--back .brand { left: 190px; top: 118px; display: flex; align-items: center; gap: 26px; }
  .card--back .brand__name { font-size: 34px; color: var(--steel-pale); }
  .card--back .brand__tagline { color: var(--steel-pale); font-size: 12px; padding-left: 38px; }
  .card--back .brand__mark { width: 62px; height: 62px; border-color: var(--steel-pale); margin: 0; }
</style>
</head>
<body>
<main class="canvas">

  <section class="card card--front" aria-label="Business card front">
    <div class="brand">
      <span class="brand__mark"></span>
      <span class="brand__name">Marlowe Pettigrew</span>
      <span class="brand__tagline">Insurance &amp; Investments</span>
    </div>

    <div class="divider divider--main"></div>
    <div class="holder">
      <div class="holder__name">Marlowe Pettigrew</div>
      <div class="holder__title">President</div>
    </div>
    <div class="divider divider--tail"></div>

    <ul class="contacts">
      <li>
        <svg class="icon" viewBox="0 0 20 20" aria-hidden="true">
          <rect width="20" height="20" rx="3" fill="#2f3858"/>
          <path d="M7 5 L9 8 L8 9.5 Q9.5 12 11 12.5 L12.5 11.5 L15 13.5 L13.5 15 Q9 15 5.5 8.5 Q5.5 6 7 5 Z" fill="#fff"/>
        </svg>
        0321 555 0147
      </li>
      <li>
        <svg class="icon" viewBox="0 0 20 20" aria-hidden="true">
          <rect width="20" height="20" rx="3" fill="#2f3858"/>
          <circle cx="10" cy="10" r="5" fill="none" stroke="#fff" stroke-width="1.2"/>
          <path d="M5 10 H15 M10 5 Q7 10 10 15 M10 5 Q13 10 10 15" fill="none" stroke="#fff" stroke-width="1"/>
        </svg>
        info@marlowepettigrew.com
      </li>
      <li>
        <svg class="icon" viewBox="0 0 20 20" aria-hidden="true">
          <rect width="20" height="20" rx="3" fill="#2f3858"/>
          <path d="M4.5 10 L10 5 L15.5 10 M6.5 9 V15 H13.5 V9" fill="none" stroke="#fff" stroke-width="1.4"/>
          <rect x="9" y="11.5" width="2" height="3.5" fill="#fff"/>
        </svg>
        marlowepettigrew.com
      </li>
    </ul>

    <div class="band"><div class="band__accent"></div></div>
  </section>

  <section class="card card--back" aria-label="Business card back">
    <div class="brand">
      <div>
        <span class="brand__name">Marlowe Pettigrew</span>
        <span class="brand__tagline">Insurance &amp; Investments</span>
      </div>
      <span class="brand__mark"></span>
    </div>
    <div class="band"><div class="band__accent"></div></div>
  </section>

</main>
</body>
</html>
```